Additional Benefits of Working for VALMIRA

Please prepare an infographic on the additional benefits besides salary of working at VALMIRA as detailed in the attached word document. Also attached is our logo in eps and our company design "Grounds". We are a Not For Profit company that finds jobs for unemployed people of government benefit payments

Tarnlee Market(s)

Attracting people to work for VALMIRA. Making VALMIRA an employer of choice.

Font styles to use
Sans Serif

Colors

Designer to choose colors to be used in the design.

Requirements
Must have
• be on 1 page
• have our logo
Nice to have
• Our Grounds design worked into it.
• Happy engaged employees
• Community engagement - we are a not for profit organisation
Should not have
• Discrimination, swearing,

```html
<!DOCTYPE html>
<html lang="en">
<head>
<meta charset="utf-8">
<title>Additional Benefits of Working for VALMIRA</title>
<link href="https://fonts.googleapis.com/css2?family=Poppins:wght@400;600;700&display=swap" rel="stylesheet">
<style>
  :root{
    --ink:#222;
    --teal:#1fbfc4;
    --yellow:#f6bd35;
    --lilac:#a9a6f0;
    --mint:#7fe3d6;
    --green:#3ee06b;
    --lime:#8bd41c;
    --violet:#6b3fb3;
    --navy:#1b4f86;
    --orange:#ff5a1f;
    --amber:#ffb02e;
    --crimson:#d8245a;
    --plum:#3a1530;
    --pink:#e0457a;
    --paper:#ffffff;
  }
  html,body{margin:0;padding:0;width:1200px;height:1200px;overflow:hidden;background:var(--paper);}
  body{font-family:"Poppins",sans-serif;color:var(--ink);}
  .infographic{position:absolute;left:73px;top:118px;width:780px;height:713px;transform:scale(1.35);transform-origin:0 0;}
  .frames{position:absolute;left:0;top:0;width:780px;height:713px;overflow:visible;}
  .card{position:absolute;width:102px;font-size:9.2px;line-height:10.6px;}
  .card p{margin:0 0 9.5px;}
  .card strong{font-weight:600;}
  .tag{position:absolute;display:flex;align-items:center;justify-content:center;text-align:center;
       color:#fff;font-weight:700;font-size:9px;line-height:9.5px;border-radius:5px;
       box-shadow:0 0 0 5px var(--paper);}
  .tag.pill{height:12px;border-radius:7px;}
  .brand{position:absolute;left:345px;top:351px;width:90px;height:22px;line-height:22px;text-align:center;
         font-weight:600;font-size:14px;color:var(--ink);letter-spacing:.3px;background:var(--paper);}
  .hl-teal{color:var(--teal)} .hl-lilac{color:var(--lilac)} .hl-green{color:var(--green)}
  .hl-purple{color:var(--violet)} .hl-navy{color:var(--navy)} .hl-orange{color:var(--orange)}
  .hl-crimson{color:var(--crimson)}
</style>
</head>
<body>
<main class="infographic" aria-label="Additional benefits of working for VALMIRA">
  <svg class="frames" viewBox="0 0 780 713" aria-hidden="true">
    <defs>
      <linearGradient id="g-life" x1="0" x2="1"><stop offset="0" stop-color="#1fbfc4"/><stop offset="1" stop-color="#f6bd35"/></linearGradient>
      <linearGradient id="g-well" x1="0" x2="1"><stop offset="0" stop-color="#7fe3d6"/><stop offset="1" stop-color="#a9a6f0"/></linearGradient>
      <linearGradient id="g-career" x1="0" x2="1"><stop offset="0" stop-color="#8bd41c"/><stop offset="1" stop-color="#3ee06b"/></linearGradient>
      <linearGradient id="g-pay" x1="0" x2="1"><stop offset="0" stop-color="#b07ee0"/><stop offset="1" stop-color="#6b3fb3"/></linearGradient>
      <linearGradient id="g-ben" x1="0" x2="1"><stop offset="0" stop-color="#6b7894"/><stop offset="1" stop-color="#3a4766"/></linearGradient>
      <linearGradient id="g-com" x1="0" x2="1"><stop offset="0" stop-color="#ff5a1f"/><stop offset="1" stop-color="#ffb02e"/></linearGradient>
      <linearGradient id="g-rec" x1="0" x2="1"><stop offset="0" stop-color="#d8245a"/><stop offset="1" stop-color="#c9304a"/></linearGradient>
      <linearGradient id="g-div" x1="0" x2="1"><stop offset="0" stop-color="#3a1530"/><stop offset="1" stop-color="#e0457a"/></linearGradient>
    </defs>

    <g class="connectors" fill="none" stroke-width="2.2" stroke-linecap="round">
      <path d="M67,302 C80,367 260,377 345,360" stroke="#f6bd35"/>
      <path d="M67,412 C70,377 160,382 260,377 S330,366 345,364" stroke="#f6bd35"/>
      <path d="M282,297 C280,347 330,352 350,356" stroke="#f6bd35"/>
      <path d="M282,419 C285,387 330,372 350,368" stroke="#f6bd35"/>
      <path d="M497,297 C490,337 460,350 435,358" stroke="#1fbfc4"/>
      <path d="M497,412 C498,372 470,368 435,366" stroke="#1fbfc4"/>
      <path d="M713,297 C710,337 600,327 520,337 C470,345 450,358 435,362" stroke="#1fbfc4"/>
      <path d="M713,412 C690,367 620,347 540,347 C480,347 455,358 435,364" stroke="#1fbfc4"/>
    </g>

    <g class="card-frames" fill="none" stroke-width="2.6">
      <rect x="1" y="2" width="130" height="287" rx="9" stroke="url(#g-life)"/>
      <rect x="217" y="2" width="130" height="287" rx="9" stroke="url(#g-well)"/>
      <rect x="433" y="2" width="129" height="287" rx="9" stroke="url(#g-career)"/>
      <rect x="648" y="2" width="130" height="287" rx="9" stroke="url(#g-pay)"/>
      <rect x="1" y="425" width="130" height="287" rx="9" stroke="url(#g-ben)"/>
      <rect x="217" y="425" width="130" height="287" rx="9" stroke="url(#g-com)"/>
      <rect x="433" y="425" width="129" height="287" rx="9" stroke="url(#g-rec)"/>
      <rect x="648" y="425" width="130" height="287" rx="9" stroke="url(#g-div)"/>
    </g>
  </svg>

  <div class="brand">VALMIRA</div>

  <section class="card" style="left:18px;top:13px;">
    <p><strong class="hl-teal">VALMIRA Day Leave</strong></p>
    <p>An extra day off at Christmas!</p>
    <p>Birthday Leave. A paid day off on your birthday</p>
    <p>A day off every month as Time In Lieu</p>
    <p><strong class="hl-teal">4 weeks</strong> Annual Leave</p>
    <p>Generous Personal Leave</p>
    <p>Support for parental leave for the birth or adoption of a child</p>
    <p><strong class="hl-teal">Flexible</strong> work arrangements</p>
  </section>
  <div class="tag pill" style="left:28px;top:282px;width:77px;background:linear-gradient(90deg,var(--teal),var(--yellow));">Life Balance</div>

  <section class="card" style="left:232px;top:14px;">
    <p>Up to <strong class="hl-lilac">$450</strong> per year to spend on Wellbeing services such as gym or yoga memberships</p>
    <p><strong class="hl-lilac">Free</strong> counselling services <strong class="hl-lilac">24x7</strong> via our Employee Assistance Program</p>
    <p>Discount private health insurance</p>
    <p>WHS policies which support a safe, inclusive work place</p>
  </section>
  <div class="tag pill" style="left:243px;top:282px;width:78px;background:linear-gradient(90deg,var(--mint),var(--lilac));">Wellbeing</div>

  <section class="card" style="left:447px;top:14px;">
    <p>Ongoing internal training and development opportunities.</p>
    <p>External study support &amp; study leave</p>
    <p>Access to the tools and technology to do your job well</p>
    <p><strong class="hl-green">Career advancement</strong> opportunities</p>
    <p>Internal job vacancy listings</p>
  </section>
  <div class="tag" style="left:459px;top:239px;width:77px;height:50px;background:linear-gradient(160deg,var(--lime),var(--green));">Career Growth<br>&amp;<br>Professional<br>Development</div>

  <section class="card" style="left:662px;top:14px;">
    <p>Competitive salary</p>
    <p>Ability to salary package up to <strong class="hl-purple">$15,900</strong> and reduce your tax. Package rent, home loans, child care and much more</p>
    <p>Salary package up to <strong class="hl-purple">$2,650</strong> on meal entertainment and holiday accommodation</p>
  </section>
  <div class="tag" style="left:674px;top:239px;width:78px;height:56px;background:linear-gradient(160deg,#c08ae6,var(--violet));">Remuneration<br>&amp;<br>Salary<br>Packaging</div>

  <div class="tag pill" style="left:28px;top:420px;width:77px;background:linear-gradient(90deg,#6b7894,#3a4766);">Benefits</div>
  <section class="card" style="left:17px;top:471px;">
    <p>Discounted vouches for:<br><strong class="hl-navy">Corrow,<br>Wellmart's,<br>KL Sonic, Reelhouse,<br>Don Merrit's,<br>Q-Store,<br>Tarnlee,<br>BTX</strong><br>and many others via Perkvault e-wallet</p>
    <p>A range of other employee discounts are also available, including access to discounted banking and finance, vehicle purchasing, leasing and hotel accommodation</p>
  </section>

  <div class="tag" style="left:243px;top:419px;width:78px;height:36px;background:linear-gradient(160deg,var(--orange),var(--amber));">Contributing<br>to<br>Community</div>
  <section class="card" style="left:232px;top:471px;">
    <p>Team involvement in local charity and community events</p>
    <p>Participation in VALMIRA's <strong class="hl-orange">1000 Jobs</strong> in 100 days initiative</p>
    <p>Strong relationships and connection with Indigenous Communities in support of Indigenous Employment</p>
  </section>

  <div class="tag pill" style="left:458px;top:420px;width:78px;background:linear-gradient(90deg,var(--crimson),#c9304a);">Recognition</div>
  <section class="card" style="left:451px;top:471px;">
    <p>We <strong class="hl-crimson">celebrate</strong> our people for reaching service milestones</p>
    <p>Team &amp; individual recognition for high performance</p>
  </section>

  <div class="tag" style="left:674px;top:422px;width:78px;height:34px;background:linear-gradient(90deg,var(--plum),var(--pink));">Diversity<br>&amp;<br>Inclusion</div>
  <section class="card" style="left:666px;top:471px;">
    <p>An inclusive and <strong class="hl-crimson">diverse</strong> culture where different backgrounds, experiences and perspectives are <strong class="hl-crimson">valued</strong></p>
    <p>Gender diversity. Over <strong class="hl-crimson">50%</strong> of our workforce and our leaders are <strong class="hl-crimson">female.</strong></p>
  </section>
</main>
</body>
</html>
```